Business Card Design Project

it should have the logo in one side
the other side

Name
Position
telephone
email

Target Market(s)

Business prospects and upscale Fashion shoppers

Industry/Entity Type

Business

Font styles to use
Serif
Sans Serif

Requirements
Must have
• very elegant, upscale, modern
Nice to have
• layering, embossed
Should not have
• Should not use any color OTHER THAN black, silver, white or purple

```html
<!DOCTYPE html>
<html lang="en">
<head>
<meta charset="UTF-8">
<title>Velora Business Card</title>
<link href="https://fonts.googleapis.com/css2?family=Questrial&display=swap" rel="stylesheet">
<style>
  :root {
    --stage: #d9d9db;
    --card-black: #050505;
    --card-white: #ffffff;
    --purple: #8e4fa8;
    --purple-deep: #5e2e73;
    --ink: #111111;
  }
  * { margin: 0; padding: 0; box-sizing: border-box; }
  html, body {
    width: 1200px;
    height: 800px;
    overflow: hidden;
  }
  body {
    background: var(--stage);
    font-family: "Questrial", "Century Gothic", sans-serif;
    position: relative;
  }
  .card {
    position: absolute;
    top: 85px;
    width: 360px;
    height: 630px;
    box-shadow: 0 6px 18px rgba(0, 0, 0, 0.25);
  }
  .card--front {
    left: 210px;
    background: var(--card-black);
    display: flex;
    align-items: center;
    justify-content: center;
  }
  .card--back {
    left: 630px;
    background: var(--card-white);
    padding: 90px 48px 0 48px;
  }
  .brand {
    display: flex;
    align-items: center;
    gap: 14px;
  }
  .brand__square {
    width: 18px;
    height: 18px;
    background: var(--purple);
  }
  .brand__name {
    font-size: 52px;
    letter-spacing: 6px;
    color: var(--purple);
    line-height: 1;
  }
  .card--back .brand__name {
    color: var(--ink);
    font-size: 46px;
  }
  .holder {
    margin-top: 120px;
  }
  .holder__name {
    font-size: 30px;
    color: var(--purple);
    letter-spacing: 1px;
    line-height: 1.1;
  }
  .holder__role {
    font-size: 19px;
    color: var(--ink);
    margin-left: 70px;
  }
  .contact {
    list-style: none;
    margin-top: 60px;
    font-size: 18px;
    color: var(--ink);
    line-height: 1.5;
  }
  .contact__label {
    color: var(--purple);
    margin-right: 6px;
  }
</style>
</head>
<body>
  <section class="card card--front" aria-label="Card front">
    <div class="brand">
      <span class="brand__square"></span>
      <span class="brand__name">VELORA</span>
    </div>
  </section>

  <section class="card card--back" aria-label="Card back">
    <div class="brand">
      <span class="brand__square"></span>
      <span class="brand__name">VELORA</span>
    </div>

    <div class="holder">
      <p class="holder__name">YOUR NAME</p>
      <p class="holder__role">Director</p>
    </div>

    <ul class="contact">
      <li><span class="contact__label">[T]</span>123 456 7890</li>
      <li><span class="contact__label">[E]</span>yourname@veloraluxury.com</li>
      <li><span class="contact__label">[W]</span>www.veloraluxury.com</li>
    </ul>
  </section>
</body>
</html>
```